Letterhead Design Project

Need Letterhead and Envelpe design with One Single or Both Side pockets for a yong dynamic employee friendly IT services company. It should be professional and sleek and should look fresh.

Target Market(s)

IT Corporate

Industry/Entity Type

It Company

```html
<!DOCTYPE html>
<html lang="en">
<head>
<meta charset="utf-8">
<title>Nexora Letterhead</title>
<link rel="stylesheet" href="https://fonts.googleapis.com/css2?family=Open+Sans:wght@400;700&display=swap">
<style>
  :root {
    --blue-deep: #1273bb;
    --blue-bright: #22a9e1;
    --orange: #f7941d;
    --red: #ef4136;
    --paper: #ffffff;
    --brand-blue: #1a86cc;
    --footer-text: #ffffff;
  }
  html, body {
    margin: 0;
    padding: 0;
    overflow: hidden;
    background: var(--paper);
  }
  .letterhead {
    position: relative;
    width: 1200px;
    height: 900px;
    overflow: hidden;
    background: var(--paper);
    font-family: "Open Sans", Arial, sans-serif;
  }
  .header-swoosh {
    position: absolute;
    top: 0;
    left: 0;
    width: 1200px;
    height: 220px;
  }
  .brand-name {
    position: absolute;
    left: 27px;
    top: 70px;
    margin: 0;
    font-size: 50px;
    font-weight: 700;
    line-height: 1;
    color: var(--brand-blue);
  }
  .footer-accent {
    position: absolute;
    left: 0;
    top: 821px;
    width: 1200px;
    height: 15px;
    background: linear-gradient(90deg, var(--red) 0%, var(--orange) 55%, var(--red) 100%);
  }
  .footer-bar {
    position: absolute;
    left: 0;
    top: 836px;
    width: 1200px;
    height: 64px;
    background: linear-gradient(90deg, var(--blue-deep) 0%, var(--blue-bright) 45%, var(--blue-deep) 100%);
  }
  .contact-list {
    position: absolute;
    top: 872px;
    left: 0;
    margin: 0;
    padding: 0;
    list-style: none;
    color: var(--footer-text);
    font-size: 17px;
    font-weight: 400;
  }
  .contact-list li { position: absolute; white-space: nowrap; }
  .contact-address { left: 400px; }
  .contact-phone { left: 493px; top: -1px; }
  .contact-person { left: 606px; }
  .contact-name { left: 718px; }
</style>
</head>
<body>
<div class="letterhead">
  <svg class="header-swoosh" viewBox="0 0 1200 220" aria-hidden="true">
    <defs>
      <linearGradient id="header-blue" x1="0" y1="0" x2="1" y2="0">
        <stop offset="0" stop-color="#1273bb"/>
        <stop offset="0.57" stop-color="#22a9e1"/>
        <stop offset="1" stop-color="#1273bb"/>
      </linearGradient>
      <linearGradient id="header-orange" x1="0" y1="0" x2="1" y2="0">
        <stop offset="0" stop-color="#ef4136"/>
        <stop offset="0.5" stop-color="#f7941d"/>
        <stop offset="1" stop-color="#ef4136"/>
      </linearGradient>
    </defs>
    <path class="swoosh-stripe" fill="url(#header-orange)"
          d="M0 42 C400 26 950 86 1200 166 V208 C960 122 450 38 0 47 Z"/>
    <path class="swoosh-band" fill="url(#header-blue)"
          d="M0 0 H1200 V162 C950 82 400 20 0 39 Z"/>
    <path class="swoosh-highlight" fill="none" stroke="#ffffff" stroke-width="2.5"
          d="M1200 164 C950 84 400 22 0 41"/>
  </svg>

  <p class="brand-name">Nexora</p>

  <div class="footer-accent"></div>
  <div class="footer-bar"></div>
  <ul class="contact-list">
    <li class="contact-address">Address</li>
    <li class="contact-phone">cell phone</li>
    <li class="contact-person">Contact</li>
    <li class="contact-name">Name</li>
  </ul>
</div>
</body>
</html>
```